Website for a new investor-focused estate agency portal

Require a website for a new investor-focused estate agency portal, this will interface with our exisitng API for data posting and retrieval. We have a logo for the business, but will happily change the colour palette to suit the design.
Requirements:
1) Landing page to describe the business
- Feature line showing the latest properties in our listings
- Announcement section (e.g. mobile app coming soon)
- Text area - what we do for Investors
- Text area - what we do for Agents and sourcers
- Text area - what we do for Home buyers
- Small Q&A
- Subscription pricing description and sign up
2) Content page (product updates page)
A timeline to list list releases, new features and other improvements to the service, website and app, shown in most recent date order.
3) A property search/result page including search form
4) A single property detail page, including
- carousel for images and video
- map
- text content
5) A data entry page to enter property data into the system. This page will contain a sidebar menu, property name, address, description, and about 10 other fields (detail to be provided). The attached screen dump files are snapshot of the wireframe form used by the development team for the property entry page.
Target Market(s)
Property investors / Real estate buyer's including personal home buyers.
Number of Pages Required
5+ page
Colors
Designer to choose colors to be used in the design.
Requirements
Must have
- Clean, crisp design and presentaion.
Nice to have
- The Search/result page (3) and the detail page (4) may have 2-3 elements for paid advertising but should also look good without those elements.
Should not have
- Must not be too busy with distracting elements

```html
<!DOCTYPE html>
<html lang="en">
<head>
<meta charset="utf-8">
<title>Northgate Homes – Find the perfect home</title>
<link href="https://fonts.googleapis.com/css2?family=Fira+Sans:wght@400;500;600;700&display=swap" rel="stylesheet">
<style>
:root{
  --brand:#2d5f7e;
  --brand-dark:#244f6a;
  --panel:#5a9fd6;
  --panel-dark:#2e5a79;
  --page:#efefef;
  --ink:#1f1f1f;
  --muted:#8a8a8a;
  --white:#ffffff;
  --footer:#000000;
  --accent:#4aa3dc;
  --rule:#5a5a5a;
}
*{box-sizing:border-box;margin:0;padding:0}
html,body{width:1200px;height:3145px;overflow:hidden}
body{position:relative;background:var(--page);font-family:"Fira Sans",Arial,sans-serif;color:var(--ink)}
.abs{position:absolute}

/* header */
.site-header{position:absolute;left:0;top:0;width:1200px;height:124px;background:var(--brand)}
.nav-link{position:absolute;top:53px;color:var(--white);font-size:13px;font-weight:600}
.brand-name{position:absolute;left:540px;top:50px;width:120px;text-align:center;color:var(--white);font-size:15px;font-weight:600;line-height:1.1}

/* hero */
.hero{position:absolute;left:0;top:124px;width:1200px;height:559px;background:linear-gradient(180deg,#3b4e62 0%,#4a5a6a 35%,#2f5f86 65%,#1d3c5c 100%)}
.hero-title{position:absolute;left:0;top:284px;width:1200px;text-align:center;color:var(--white);font-size:26px;font-weight:600}
.search-panel{position:absolute;left:244px;top:348px;width:712px;height:171px;background:rgba(35,80,115,.82)}
.search-tab{position:absolute;top:12px;width:178px;text-align:center;color:var(--white);font-size:14px}
.tab-rule{position:absolute;left:0;top:41px;width:712px;height:1px;background:rgba(255,255,255,.5)}
.tab-active{position:absolute;left:0;top:40px;width:178px;height:3px;background:var(--white)}
.search-input{position:absolute;left:11px;top:57px;width:576px;height:32px;background:var(--white);color:#9a9a9a;font-size:12px;padding:9px 8px}
.search-btn{position:absolute;left:587px;top:57px;width:110px;height:32px;background:#0f1a22;color:var(--white);font-size:13px;display:flex;align-items:center;justify-content:center;gap:5px}
.filters{position:absolute;left:11px;top:101px;width:686px;height:64px;background:var(--panel);border-radius:3px;display:flex}
.filter{flex:1;position:relative;color:var(--white);border-right:1px solid rgba(255,255,255,.35);padding:10px 12px}
.filter:last-child{border-right:none}
.filter small{display:block;font-size:11px}
.filter b{display:block;font-size:13px;font-weight:500;margin-top:8px}
.filter svg{position:absolute;right:12px;top:33px}
.hero-arrow{position:absolute;top:383px}
.dots{position:absolute;left:576px;top:596px;display:flex;gap:6px}
.dot{width:9px;height:9px;background:var(--white);transform:rotate(45deg)}
.dot.on{background:var(--panel)}

/* intro sections */
.section-title{position:absolute;left:0;width:1200px;text-align:center;font-size:21px;font-weight:600;color:var(--ink)}
.title-rule{position:absolute;left:556px;width:88px;height:3px;background:var(--brand)}
.section-text{position:absolute;left:316px;width:568px;text-align:center;font-size:9.5px;line-height:12px;color:var(--muted)}

/* property cards */
.card{position:absolute;overflow:hidden;color:var(--white);text-align:center}
.card-title{font-size:16px;font-weight:600;margin-top:46px}
.card-text{font-size:8.5px;line-height:10px;margin:14px auto 0}
.card.wide-a{background:linear-gradient(135deg,#26384d 0%,#4d5a66 50%,#1f3146 100%)}
.card.wide-b{background:linear-gradient(160deg,#3b4d66 0%,#8a7a6a 55%,#5b5048 100%)}
.card.villa{background:linear-gradient(180deg,#6f8fae 0%,#7c6a55 45%,#3e4a3a 75%,#2f3f4e 100%)}
.card.palms{background:linear-gradient(180deg,#2c3e5a 0%,#5b5a4a 45%,#344a2e 80%,#2a3a26 100%)}
.card .shade{position:absolute;inset:0;background:rgba(0,0,0,.25)}
.card .inner{position:relative}

/* contact */
.contact-line{position:absolute;left:233px;font-size:11px;color:var(--muted)}
.map{position:absolute;left:187px;top:2368px;width:372px;height:173px;background:linear-gradient(135deg,#e4e4e4,#f4f4f4 50%,#dcdcdc)}
.field{position:absolute;left:607px;width:385px;background:var(--white);font-size:11px;color:var(--muted);padding:15px 16px}
.submit{position:absolute;left:607px;top:2497px;width:385px;height:44px;border-radius:22px;background:var(--brand);color:var(--white);font-size:16px;font-weight:600;display:flex;align-items:center;justify-content:center}

/* newsletter */
.signup{position:absolute;left:0;top:2604px;width:1200px;height:130px;background:var(--brand)}
.signup-title{position:absolute;left:283px;top:50px;color:var(--white);font-size:22px;font-weight:600}
.signup-input{position:absolute;left:590px;top:32px;width:223px;height:31px;background:var(--white);color:#a0a0a0;font-size:11px;padding:9px 12px}
.signup-btn{position:absolute;left:840px;top:32px;width:76px;height:31px;background:#000;color:var(--white);font-size:12px;font-weight:600;display:flex;align-items:center;justify-content:center}
.consent{position:absolute;left:590px;top:88px;color:var(--white);font-size:7.5px;display:flex;align-items:center;gap:5px}
.consent i{width:7px;height:7px;background:var(--white);display:block}

/* footer */
.site-footer{position:absolute;left:0;top:2734px;width:1200px;height:411px;background:var(--footer);color:var(--white)}
.footer-heading{position:absolute;left:187px;color:var(--accent);font-size:13px;font-weight:500}
.footer-rule{position:absolute;left:187px;width:826px;height:2px;background:var(--rule)}
.footer-link{position:absolute;font-size:9.5px}
.copyright{position:absolute;left:187px;top:350px;font-size:10.5px}
.social{position:absolute;top:349px;width:23px;height:23px;border-radius:50%;background:var(--accent)}
.to-top{position:absolute;left:1087px;top:187px;width:37px;height:37px;border:2px solid var(--accent);border-radius:50%;display:flex;align-items:center;justify-content:center}
</style>
</head>
<body>

<header class="site-header">
  <span class="nav-link" style="left:187px">For sale</span>
  <span class="nav-link" style="left:277px">To rent</span>
  <span class="nav-link" style="left:363px">House prices</span>
  <span class="nav-link" style="left:481px">Invest</span>
  <span class="brand-name">Northgate Homes</span>
  <span class="nav-link" style="left:669px">New homes</span>
  <span class="nav-link" style="left:765px">Commercial</span>
  <span class="nav-link" style="left:864px">Overseas</span>
  <span class="nav-link" style="left:946px">Find agents</span>
</header>

<section class="hero" role="img" aria-label="Modern white villa with glass walls and an illuminated pool at dusk"></section>
<h1 class="hero-title">Find the perfect home to buy or rent in the UK</h1>
<svg class="hero-arrow" style="left:82px" width="24" height="40" viewBox="0 0 24 40"><path d="M21 2 3 20l18 18" fill="none" stroke="#fff" stroke-width="2.5"/></svg>
<svg class="hero-arrow" style="left:1094px" width="24" height="40" viewBox="0 0 24 40"><path d="M3 2l18 18L3 38" fill="none" stroke="#fff" stroke-width="2.5"/></svg>

<form class="search-panel">
  <span class="search-tab" style="left:0">For sale</span>
  <span class="search-tab" style="left:178px">To rent</span>
  <span class="search-tab" style="left:356px">Find agents</span>
  <span class="search-tab" style="left:534px">Sold prices</span>
  <span class="tab-rule"></span><span class="tab-active"></span>
  <div class="search-input">e.g. Bristol, SW6, G61 2DW, Victoria Station</div>
  <div class="search-btn"><svg width="12" height="12" viewBox="0 0 12 12"><circle cx="5" cy="5" r="3.8" fill="none" stroke="#fff" stroke-width="1.3"/><path d="M8 8l3 3" stroke="#fff" stroke-width="1.3"/></svg>Search</div>
  <div class="filters">
    <div class="filter"><small>Min price ($)</small><b>Any</b><svg width="14" height="8" viewBox="0 0 14 8"><path d="M1 1l6 6 6-6" fill="none" stroke="#fff" stroke-width="2"/></svg></div>
    <div class="filter"><small>Max price ($)</small><b>Any</b><svg width="14" height="8" viewBox="0 0 14 8"><path d="M1 1l6 6 6-6" fill="none" stroke="#fff" stroke-width="2"/></svg></div>
    <div class="filter"><small>Property type</small><b>Any</b><svg width="14" height="8" viewBox="0 0 14 8"><path d="M1 1l6 6 6-6" fill="none" stroke="#fff" stroke-width="2"/></svg></div>
    <div class="filter"><small>Bed rooms</small><b>Any</b><svg width="14" height="8" viewBox="0 0 14 8"><path d="M1 1l6 6 6-6" fill="none" stroke="#fff" stroke-width="2"/></svg></div>
  </div>
</form>
<div class="dots"><span class="dot"></span><span class="dot on"></span><span class="dot"></span></div>

<h2 class="section-title" style="top:774px">What We Do For Investors</h2>
<span class="title-rule" style="top:812px"></span>
<p class="section-text" style="top:837px">We give investors a clear view of yield, growth and risk across every listing on the portal. Live rental data, price history and local demand figures sit beside each property, so you can compare deals side by side. Saved searches alert you the moment a match appears, and our agent network helps you move quickly from first viewing through to completion with fewer surprises along the way.</p>

<h2 class="section-title" style="top:961px">What We Do For Agents And Sourcers</h2>
<span class="title-rule" style="top:999px"></span>
<p class="section-text" style="top:1024px">Agents and sourcers can post stock straight into the portal through our open API or the simple entry form. Each listing reaches a focused audience of active buyers and investors, not casual browsers. Track views, enquiries and saved listings from one dashboard, update prices in seconds, and build lasting relationships with clients who return to the portal again and again for their next purchase.</p>

<h2 class="section-title" style="top:1149px">What We Do For Home Buyers</h2>
<span class="title-rule" style="top:1187px"></span>
<p class="section-text" style="top:1212px">Home buyers get an honest, uncluttered search with the details that matter most. Filter by price, property type and bedrooms, explore local schools and transport, and view floor plans, photos and video in one place. Set up alerts for new homes in your chosen areas, book viewings online and speak directly with the agent, so finding your next home feels calm and simple from start to finish.</p>

<h2 class="section-title" style="top:1336px">Property Inspiration</h2>
<span class="title-rule" style="top:1374px"></span>

<article class="card wide-a" style="left:187px;top:1422px;width:498px;height:199px" role="img" aria-label="Open plan living room with floor to ceiling glass and pool view">
  <div class="shade"></div><div class="inner"><h3 class="card-title">The Dream Homes</h3>
  <p class="card-text" style="width:420px">A calm retreat with open living spaces, floor to ceiling glass and a heated pool set within landscaped gardens. Moments from local shops, schools and transport links, with room to grow for years to come.</p></div>
</article>
<article class="card wide-b" style="left:697px;top:1422px;width:315px;height:199px" role="img" aria-label="Terrace lounge overlooking palm trees at sunset">
  <div class="shade"></div><div class="inner"><h3 class="card-title">The Dream Homes</h3>
  <p class="card-text" style="width:260px">A calm retreat with open living spaces, floor to ceiling glass and a heated pool set within landscaped gardens. Moments from local shops, schools and transport links, with room to grow for years to come.</p></div>
</article>

<article class="card villa" style="left:187px;top:1634px;width:267px;height:219px" role="img" aria-label="Mediterranean villa with terracotta roof beside a pool"><div class="shade"></div><div class="inner"><h3 class="card-title">The Dream Homes</h3><p class="card-text" style="width:222px">Classic villa with terracotta roof, sunny terraces and mature palms. Generous rooms, a private garden and easy access to the town centre make it ideal for families and investors alike.</p></div></article>
<article class="card palms" style="left:466px;top:1634px;width:268px;height:219px" role="img" aria-label="Lit villa among palm trees at dusk"><div class="shade"></div><div class="inner"><h3 class="card-title">The Dream Homes</h3><p class="card-text" style="width:222px">Classic villa with terracotta roof, sunny terraces and mature palms. Generous rooms, a private garden and easy access to the town centre make it ideal for families and investors alike.</p></div></article>
<article class="card villa" style="left:746px;top:1634px;width:266px;height:219px" role="img" aria-label="Mediterranean villa with terracotta roof beside a pool"><div class="shade"></div><div class="inner"><h3 class="card-title">The Dream Homes</h3><p class="card-text" style="width:222px">Classic villa with terracotta roof, sunny terraces and mature palms. Generous rooms, a private garden and easy access to the town centre make it ideal for families and investors alike.</p></div></article>

<article class="card villa" style="left:187px;top:1866px;width:267px;height:220px" role="img" aria-label="Mediterranean villa with terracotta roof beside a pool"><div class="shade"></div><div class="inner"><h3 class="card-title">The Dream Homes</h3><p class="card-text" style="width:222px">Classic villa with terracotta roof, sunny terraces and mature palms. Generous rooms, a private garden and easy access to the town centre make it ideal for families and investors alike.</p></div></article>
<article class="card palms" style="left:466px;top:1866px;width:268px;height:220px" role="img" aria-label="Lit villa among palm trees at dusk"><div class="shade"></div><div class="inner"><h3 class="card-title">The Dream Homes</h3><p class="card-text" style="width:222px">Classic villa with terracotta roof, sunny terraces and mature palms. Generous rooms, a private garden and easy access to the town centre make it ideal for families and investors alike.</p></div></article>
<article class="card villa" style="left:746px;top:1866px;width:266px;height:220px" role="img" aria-label="Mediterranean villa with terracotta roof beside a pool"><div class="shade"></div><div class="inner"><h3 class="card-title">The Dream Homes</h3><p class="card-text" style="width:222px">Classic villa with terracotta roof, sunny terraces and mature palms. Generous rooms, a private garden and easy access to the town centre make it ideal for families and investors alike.</p></div></article>

<h2 class="section-title" style="top:2167px">Contact Us</h2>
<span class="title-rule" style="top:2205px"></span>

<svg class="abs" style="left:192px;top:2266px" width="14" height="22" viewBox="0 0 14 22"><path d="M7 0C3 0 0 3 0 7c0 5 7 15 7 15s7-10 7-15c0-4-3-7-7-7z" fill="#2d5f7e"/><circle cx="7" cy="7" r="2.6" fill="#efefef"/></svg>
<span class="contact-line" style="top:2272px">48 Harbour Row, Elmsford QLD 4100</span>
<svg class="abs" style="left:187px;top:2317px" width="24" height="17" viewBox="0 0 24 17"><rect width="24" height="17" fill="#2d5f7e"/><path d="M1 1l11 9 11-9" fill="none" stroke="#efefef" stroke-width="1.6"/></svg>
<span class="contact-line" style="top:2319px">hello@northgatehomes.example</span>
<div class="map" role="img" aria-label="Street map of the office location"></div>

<div class="field" style="top:2264px;height:44px">Name</div>
<div class="field" style="top:2329px;height:44px">Email</div>
<div class="field" style="top:2393px;height:85px;padding-top:12px">Message</div>
<div class="submit">SUBMIT</div>

<section class="signup">
  <h2 class="signup-title">Sign up for pricing update</h2>
  <div class="signup-input">Enter Email</div>
  <div class="signup-btn">Submit</div>
  <div class="consent"><i></i>I agree that my submitted data is being collected and stored.</div>
</section>

<footer class="site-footer">
  <h3 class="footer-heading" style="top:57px">Explore Your Company</h3>
  <span class="footer-rule" style="top:82px"></span>
  <span class="footer-link" style="left:187px;top:99px">Help</span>
  <span class="footer-link" style="left:187px;top:123px">Contact us</span>
  <span class="footer-link" style="left:187px;top:147px">Sitemap</span>
  <span class="footer-link" style="left:187px;top:171px">Terms of use</span>
  <span class="footer-link" style="left:380px;top:99px">For sale</span>
  <span class="footer-link" style="left:380px;top:123px">For rent</span>
  <span class="footer-link" style="left:380px;top:147px">House prices</span>
  <span class="footer-link" style="left:380px;top:171px">Slavery Statement</span>
  <span class="footer-link" style="left:574px;top:99px">New homes</span>
  <span class="footer-link" style="left:574px;top:123px">Commercial</span>
  <span class="footer-link" style="left:574px;top:147px">Overseas</span>
  <span class="footer-link" style="left:574px;top:171px">Invest</span>
  <span class="footer-link" style="left:768px;top:99px">Property News</span>
  <span class="footer-link" style="left:768px;top:123px">Guides</span>
  <span class="footer-link" style="left:768px;top:147px">Privacy</span>
  <span class="footer-link" style="left:768px;top:171px">Commercial</span>

  <h3 class="footer-heading" style="top:205px">Build your business</h3>
  <span class="footer-rule" style="top:229px"></span>
  <span class="footer-link" style="left:187px;top:247px">Agents &amp; Developers</span>
  <span class="footer-link" style="left:187px;top:271px">About us</span>
  <span class="footer-link" style="left:187px;top:295px">RidgeviewPro</span>
  <span class="footer-link" style="left:380px;top:247px">Display advertising</span>
  <span class="footer-link" style="left:380px;top:271px">Member T&amp;Cs</span>
  <span class="footer-link" style="left:380px;top:295px">Data feeds</span>
  <span class="footer-link" style="left:574px;top:247px">Partnerships</span>
  <span class="footer-link" style="left:574px;top:271px">API</span>
  <span class="footer-link" style="left:574px;top:295px">Jobs</span>
  <span class="footer-link" style="left:768px;top:247px">Useful Tools</span>
  <span class="footer-link" style="left:768px;top:271px">Press</span>
  <span class="footer-link" style="left:768px;top:295px">Invest</span>

  <div class="to-top"><svg width="18" height="11" viewBox="0 0 18 11"><path d="M1 10l8-8 8 8" fill="none" stroke="#4aa3dc" stroke-width="2"/></svg></div>

  <p class="copyright">© Copyright 2019 by northgatehomes.example | All Rights Reserved.</p>
  <span class="social" style="left:865px"></span>
  <span class="social" style="left:896px"></span>
  <span class="social" style="left:927px"></span>
  <span class="social" style="left:958px"></span>
  <span class="social" style="left:989px"></span>
</footer>

</body>
</html>
```